Publisher needs a book cover design for Workflow Insight Methods book

We need a book cover (front, back, spine) for the 3rd edition of a book entitled 'Workflow Insight Methods' and subtitled 'covering Structure, Design, Oversight and Growth Stages'. The author is Malcolm Feverill. The publisher is Halvenmoor Press. The finished size of the paperback version will be the industry standard 9" x 6". There will be paperback, hardback, and Kindle versions. The final number of pages is expected to be in the region 300-350 pages. Text for the back cover is not yet available, but at the bottom of the back cover should be publisher logo on the left and space for the ISBN bar code on the right.<br/>The design should be original and not include any stock images that have been created by someone else or may require obtaining a copyright licence to use. Symbols in common use and not copyrighted are probably ok.<br/>There are no required images, photographs or symbols except the publisher logo at the left bottom of the back cover and lower spine. S[ine lettering should be UK/US style with the top of the writing nearest the front cover. The designer is free to be creative using appropriate diagrams, symbols or abstract designs. Rectangular and circular variants of the publisher logo are attached.<br/>I just want to assure designers that when evaluating designs from my perspective, I take absolutely no notice whatsoever of a designer's Artisan Pool ranking or status; I am completely output driven, so what matters to me is the design, not the ranking or status of the designer. In a similar way, I do not evaluate designs as 'good' or 'bad' - the winning design will be chosen after review by a design panel.
Updates

More time is needed to check the use of stock images by designers. Some have been used by desitgners but not yet disclosed.

Target Market(s)

Practitioners and academics concerned with Workflow Insight Methods, Business Process Management, Business Process Architecture, Enterprise Architecture, Information Architecture, Process modelling, data modelling

Font styles to use
Serif
Sans Serif

Colors

Designer to choose colors to be used in the design.

Requirements
Must have
• Title, author, edition, subtitle, publisher logo.
Nice to have
• Originality, innovation
Should not have
• Stock images or anything else requiring additional copyright discussions and negotiations.

```html
<!DOCTYPE html>
<html lang="en">
<head>
<meta charset="utf-8">
<title>Workflow Insight Methods – Cover</title>
<link rel="stylesheet" href="https://fonts.googleapis.com/css2?family=Cinzel:wght@700&family=Marcellus&family=Encode+Sans+Condensed:wght@400&family=EB+Garamond:wght@500&display=swap">
<style>
  :root {
    --stage: #e7e7e5;
    --cover-dark: #262522;
    --cover-dark-deep: #141412;
    --band-light: #f4f4f2;
    --ink: #2b2a27;
    --paper-text: #f1f0ec;
    --glow-core: #f7b53a;
    --glow-mid: #a8561a;
    --glass: #3c3a36;
  }
  * { margin: 0; padding: 0; box-sizing: border-box; }
  html, body {
    width: 1200px;
    height: 1000px;
    overflow: hidden;
    background: var(--stage);
  }
  .canvas {
    position: relative;
    width: 1200px;
    height: 1000px;
  }
  .cover {
    position: absolute;
    left: 320px;
    top: 80px;
    width: 560px;
    height: 840px;
    background: linear-gradient(180deg, var(--cover-dark) 0%, var(--cover-dark-deep) 100%);
    overflow: hidden;
    box-shadow: 0 6px 24px rgba(0,0,0,0.18);
  }
  .edition-band {
    position: absolute;
    left: 0; top: 0;
    width: 100%;
    height: 72px;
    background: var(--cover-dark);
  }
  .edition {
    position: absolute;
    right: 24px;
    top: 34px;
    font-family: "EB Garamond", serif;
    font-variant-numeric: lining-nums;
    font-weight: 500;
    font-size: 23px;
    color: var(--paper-text);
  }
  .title-band {
    position: absolute;
    left: 0; top: 72px;
    width: 100%;
    height: 208px;
    background: var(--band-light);
  }
  .title {
    position: absolute;
    left: 0; top: 26px;
    width: 100%;
    text-align center;
    text-align: center;
    font-family: "Cinzel", serif;
    font-weight: 700;
    font-size: 50px;
    line-height: 80px;
    color: var(--ink);
  }
  .title span { display: block; }
  .subtitle {
    position: absolute;
    left: 0; top: 292px;
    width: 100%;
    text-align: center;
    font-family: "Encode Sans Condensed", sans-serif;
    font-weight: 400;
    font-size: 31px;
    line-height: 42px;
    color: var(--paper-text);
  }
  .subtitle span { display: block; }
  .bulb-art {
    position: absolute;
    left: 130px;
    top: 380px;
    width: 300px;
    height: 360px;
    border-radius: 150px 150px 40px 40px;
    background:
      radial-gradient(ellipse 70px 90px at 50% 35%, var(--glow-core) 0%, var(--glow-mid) 45%, transparent 100%),
      radial-gradient(ellipse 150px 180px at 50% 40%, var(--glass) 0%, transparent 100%);
  }
  .author {
    position: absolute;
    left: 0; top: 748px;
    width: 100%;
    text-align: center;
    font-family: "Marcellus", serif;
    font-size: 50px;
    color: var(--paper-text);
  }
</style>
</head>
<body>
  <main class="canvas">
    <section class="cover">
      <div class="edition-band">
        <p class="edition">3rd Edition</p>
      </div>
      <div class="title-band">
        <h1 class="title"><span>WORKFLOW</span><span>INSIGHT METHODS</span></h1>
      </div>
      <h2 class="subtitle"><span>covering Structure, Design,</span><span>Oversight and Growth Stages</span></h2>
      <div class="bulb-art" role="img" aria-label="Glowing filament light bulb on a dark background"></div>
      <p class="author">Malcolm Feverill</p>
    </section>
  </main>
</body>
</html>
```